**** Web design project for VornaSoft ****

For my ICT company VornaSoft I need a website.

We design, build and host web-applications and we have our own CMS product. In the references part we want to show sample websites (thumbnails) + links.

It should look modern (WEB 2.0), rounded corners.

I want the following menu' s:
- Home
- Services
- References
- News
- About VornaSoft
- Contact

Sample websites:
See attachments
http://www.plumvest.com
http://www.gadomirbureauwerk.nl

Reason: Want to take some time for feedback and improvements.

Reason: I'm waiting for a black background, with shadow and ambient light. You'll make a good chance!

Industry/Entity Type

It Company

Requirements
Must have
• - Fixed width (1024px), should fit on an IPad2
- Language selection English/Dutch
- Twitter/Facebook/LinkedIn/RSS icons
- Footer for Terms of use and Copyrights
- Search box
- 3 (or more) boxes for information i.e. news, blog or advertisements
Nice to have
• - Footer Site Map
- Contrasting background outside borders
- wide image (rotator) (with transperant sentence block)
- Shadow

```html
<!DOCTYPE html>
<html lang="en">
<head>
<meta charset="utf-8">
<title>VornaSoft – We design, build and host web-applications</title>
<link href="https://fonts.googleapis.com/css2?family=Roboto:wght@400;500;700&family=PT+Sans:wght@400&display=swap" rel="stylesheet">
<style>
:root{
  --ink:#1c1d22;
  --ink-soft:#25262c;
  --page:#f3f3f3;
  --cyan:#1fb4f0;
  --cyan-dark:#0e95d6;
  --text:#333333;
  --muted:#8a8a8a;
  --foot-text:#9a9ca3;
  --line:#3a3b42;
  --white:#ffffff;
}
*{margin:0;padding:0;box-sizing:border-box}
html,body{width:1095px;height:1200px;overflow:hidden}
body{position:relative;background:var(--page);font-family:"Roboto",Arial,sans-serif;color:var(--text)}
.abs{position:absolute}

.site-header{position:absolute;left:0;top:0;width:1095px;height:139px;background:var(--ink)}
.brand{left:43px;top:40px;display:flex;align-items:center;gap:18px}
.brand-mark{width:80px;height:80px;border-radius:50%;background:var(--cyan)}
.brand-name{font-size:44px;font-weight:400;color:#9bb4c4;letter-spacing:1px}

.search{left:769px;top:42px;width:160px;height:28px;border-radius:6px;background:linear-gradient(#fff,#e2e2e2);font-size:13px;color:#555;padding:6px 10px}
.search-go{left:937px;top:42px;width:33px;height:29px;border-radius:4px;background:var(--cyan);color:#fff;font-size:12px;font-weight:700;text-align:center;line-height:29px}
.social{top:86px;width:25px;height:25px;border-radius:4px}
.lang{left:872px;top:91px;font-size:15px;color:#e0e0e0}
.lang span{border-left:1px solid #aaa;padding-left:3px;margin-left:2px}

.main-nav{left:117px;top:121px;width:853px;height:43px;display:flex;border-radius:4px;overflow:hidden;background:linear-gradient(#fafafa,#e6e6e6);box-shadow:0 2px 4px rgba(0,0,0,.15)}
.main-nav a{display:block;height:43px;line-height:43px;text-align:center;font-size:17px;color:#444;text-decoration:none;border-right:1px solid #d2d2d2}
.main-nav a:last-child{border-right:0}
.main-nav a.active{background:linear-gradient(#3cc6f7,#12a6e6);color:#fff}

.hero{left:118px;top:199px;width:868px;height:321px;border-radius:4px;overflow:hidden;display:flex}
.hero-visual{width:591px;height:321px;background:linear-gradient(160deg,#e98a16 0%,#c45a08 40%,#3a3a3a 70%,#d9d9d9 100%)}
.spotlight{width:277px;height:321px;background:var(--ink);padding:50px 24px 0 24px;position:relative}
.spotlight h2{font-size:29px;font-weight:700;color:#fff;margin-bottom:8px}
.spotlight p{font-size:13px;line-height:18.5px;color:#d4d4d4}
.spotlight .cta{position:absolute;left:24px;top:219px;width:138px;height:31px;background:var(--cyan);color:#fff;font-size:13px;line-height:31px;text-align:center;border-radius:2px}
.dots{position:absolute;left:26px;top:292px;display:flex;gap:4px}
.dots i{width:11px;height:11px;border-radius:50%;background:#8a8a8a}
.dots i.on{background:var(--cyan)}

.headline{left:124px;top:536px;font-size:69px;line-height:68px;font-weight:400;color:#2d2d2d;letter-spacing:-1px}

.feature{top:709px;width:284px}
.feature-icon{width:65px;height:67px;border-radius:3px;background:linear-gradient(#38c4f6,#109fe0);display:flex;align-items:center;justify-content:center}
.feature-title{position:absolute;left:82px;top:15px;font-size:20px;font-weight:700;color:#333}
.feature-sub{position:absolute;left:82px;top:38px;font-size:15px;color:var(--muted)}
.feature p{margin-top:20px;font-family:"PT Sans",Arial,sans-serif;font-size:12.6px;line-height:18.5px;color:#222}
.read-more{display:inline-block;margin-top:15px;font-family:"PT Sans",Arial,sans-serif;font-size:12.5px;color:var(--cyan);border-bottom:1px dotted var(--cyan)}

.site-footer{position:absolute;left:0;top:958px;width:1095px;height:242px;background:var(--ink)}
.foot-line{top:1027px;height:1px;background:var(--line)}
.foot-head{top:1000px;font-size:15px;font-weight:700;color:#e8e8e8}
.foot-link{font-size:14px;color:var(--foot-text)}
.copyright{left:0;width:1134px;top:1157px;text-align:center;font-size:15px;color:#c8c8c8}
</style>
</head>
<body>

<header class="site-header"></header>
<div class="abs brand"><span class="brand-mark"></span><span class="brand-name">VornaSoft</span></div>
<div class="abs search">Enter Search</div>
<div class="abs search-go">Go</div>
<span class="abs social" style="left:771px;background:#3b5a9a"></span>
<span class="abs social" style="left:803px;background:#3cb0e4"></span>
<span class="abs social" style="left:837px;background:#f08a1c"></span>
<div class="abs lang">English<span>Dutch</span></div>

<nav class="abs main-nav">
  <a class="active" style="width:138px">Home</a>
  <a style="width:148px">Services</a>
  <a style="width:141px">References</a>
  <a style="width:131px">News</a>
  <a style="width:155px">About VornaSoft</a>
  <a style="width:140px">Contact</a>
</nav>

<section class="abs hero">
  <div class="hero-visual" role="img" aria-label="Showcase of a hosting website design with pricing packages"></div>
  <div class="spotlight">
    <h2>Spotlight Box</h2>
    <p>Lorem ipsum dolor sit amet, consectetur adipisicing elit, sed do eiusmod tempor incididunt ut labore et dolore magna aliqua. Ut enim ad minim veniam, quis nostrud exercitation. Trim ad minim veniam, quis nostrud exercitation.</p>
    <span class="cta">view our portfolio</span>
    <div class="dots"><i class="on"></i><i></i><i></i></div>
  </div>
</section>

<h1 class="abs headline">We design, build and host<br>web-applications...</h1>

<article class="abs feature" style="left:117px">
  <div class="feature-icon">
    <svg width="36" height="36" viewBox="0 0 36 36" fill="none" stroke="#fff" stroke-width="2.5"><rect x="5" y="15" width="26" height="14"/><path d="M18 30v4M12 34h12" /><path d="M18 2v9M14 7l4 4 4-4"/></svg>
  </div>
  <div class="feature-title">What we offer?</div>
  <div class="feature-sub">our work</div>
  <p>Lorem ipsum dolor sit amet, consec tetuer adipiscing elit. Praesent vestibulum molestie lacus. Aenean nonummy hendrerit mauris. Phasellus porta. Fusce suscipit varius mi.</p>
  <span class="read-more">Read More</span>
</article>

<article class="abs feature" style="left:412px">
  <div class="feature-icon">
    <svg width="36" height="36" viewBox="0 0 36 36" fill="#fff"><circle cx="15" cy="15" r="8"/><g stroke="#fff" stroke-width="4"><path d="M15 3v24M3 15h24M6.5 6.5l17 17M23.5 6.5l-17 17"/></g><circle cx="15" cy="15" r="3.5" fill="#1aaeea"/><circle cx="28" cy="28" r="5"/><circle cx="28" cy="28" r="2" fill="#1aaeea"/></svg>
  </div>
  <div class="feature-title">How does it work?</div>
  <div class="feature-sub">our solutions</div>
  <p>Lorem ipsum dolor sit amet, consec tetuer adipiscing elit. Praesent vestibulum molestie lacus. Aenean nonummy hendrerit mauris. Phasellus porta. Fusce suscipit varius mi.</p>
  <span class="read-more">Read More</span>
</article>

<article class="abs feature" style="left:707px">
  <div class="feature-icon">
    <svg width="40" height="32" viewBox="0 0 40 32" fill="#fff"><circle cx="20" cy="8" r="5"/><path d="M11 28c0-8 4-12 9-12s9 4 9 12z"/><circle cx="8" cy="11" r="4"/><path d="M1 28c0-6 3-10 7-10 2 0 3 1 4 2-1 2-2 5-2 8z"/><circle cx="32" cy="11" r="4"/><path d="M39 28c0-6-3-10-7-10-2 0-3 1-4 2 1 2 2 5 2 8z"/></svg>
  </div>
  <div class="feature-title">Why choose us?</div>
  <div class="feature-sub">our advantages</div>
  <p>Lorem ipsum dolor sit amet, consec tetuer adipiscing elit. Praesent vestibulum molestie lacus. Aenean nonummy hendrerit mauris. Phasellus porta. Fusce suscipit varius mi.</p>
  <span class="read-more">Read More</span>
</article>

<footer class="site-footer"></footer>
<div class="abs foot-line" style="left:74px;width:168px"></div>
<div class="abs foot-line" style="left:260px;width:130px"></div>
<div class="abs foot-line" style="left:408px;width:131px"></div>
<div class="abs foot-line" style="left:557px;width:103px"></div>
<div class="abs foot-line" style="left:678px;width:152px"></div>
<div class="abs foot-line" style="left:850px;width:140px"></div>

<div class="abs foot-head" style="left:163px">Home</div>
<div class="abs foot-head" style="left:298px">Services</div>
<div class="abs foot-head" style="left:434px">References</div>
<div class="abs foot-head" style="left:589px">News</div>
<div class="abs foot-head" style="left:699px">About VornaSoft</div>
<div class="abs foot-head" style="left:868px">Contact</div>

<div class="abs foot-link" style="left:160px;top:1042px">Page 1</div>
<div class="abs foot-link" style="left:160px;top:1068px">Page 2</div>
<div class="abs foot-link" style="left:160px;top:1094px">Page 3</div>
<div class="abs foot-link" style="left:298px;top:1042px">Services</div>
<div class="abs foot-link" style="left:434px;top:1042px">References</div>
<div class="abs foot-link" style="left:589px;top:1042px">News</div>
<div class="abs foot-link" style="left:699px;top:1042px">About VornaSoft</div>
<div class="abs foot-link" style="left:870px;top:1042px">Contact</div>

<div class="abs copyright">© 2012 VornaSoft, All Rights Reserved.</div>

</body>
</html>
```